Hydrographic business needs a business card that reaches hunters and off-road enthusiasts

We need a business card for a new hydrographics company catering to customers such as hunters, off-road ATV riders and custom vehicle enthusiasts. A western theme is preferred but professional. Our service should be thought of as upper end graphic design on firearms, off road vehicles, motorcycles, etc... See www.caldorfx.com for ideas on patterns, colors, etc...

Target Market(s)

Hunters, off road enthusiasts, custom car enthusiasts, motorcycle riders...

Industry/Entity Type

Graphic Design

```html
<!DOCTYPE html>
<html lang="en">
<head>
<meta charset="utf-8">
<title>Caldor Hydro Graphics – Business Card</title>
<link rel="stylesheet" href="https://fonts.googleapis.com/css2?family=Open+Sans:wght@400;600;700&display=swap">
<style>
  :root {
    --backdrop: #e4e2df;
    --card-front: #ffffff;
    --card-back: #2e2b2b;
    --card-back-emboss: #242121;
    --ink: #1e1e1e;
    --ink-soft: #2b2b2b;
    --rule: #c9c9c9;
  }
  * { margin: 0; padding: 0; box-sizing: border-box; }
  html, body {
    width: 1200px;
    height: 900px;
    overflow: hidden;
    background: var(--backdrop);
    font-family: "Open Sans", Arial, sans-serif;
  }
  .sheet {
    width: 1200px;
    height: 900px;
    display: flex;
    flex-direction: column;
    align-items: center;
    justify-content: center;
    gap: 24px;
  }
  .card {
    width: 700px;
    height: 400px;
    border-radius: 3px;
    box-shadow: 0 2px 8px rgba(0,0,0,0.18);
    display: flex;
    flex-direction: column;
    align-items: center;
  }
  .card--back {
    background: var(--card-back);
    justify-content: center;
  }
  .card--back .brand-name {
    color: var(--card-back-emboss);
    font-size: 44px;
  }
  .card--front {
    background: var(--card-front);
    padding-top: 62px;
  }
  .brand-name {
    font-weight: 600;
    font-size: 42px;
    letter-spacing: 0.5px;
    color: var(--ink);
  }
  .holder-name {
    margin-top: 34px;
    font-weight: 700;
    font-size: 25px;
    color: var(--ink);
  }
  .divider {
    width: 190px;
    height: 1px;
    background: var(--rule);
    margin: 12px 0 14px;
  }
  .contact {
    font-size: 16.5px;
    line-height: 1.3;
    color: var(--ink-soft);
    text-align: center;
  }
  .contact--reach { margin-top: 14px; }
  .contact .domain { font-weight: 700; }
</style>
</head>
<body>
  <main class="sheet">
    <section class="card card--back" aria-label="Card back">
      <p class="brand-name">Caldor Hydro Graphics</p>
    </section>

    <section class="card card--front" aria-label="Card front">
      <p class="brand-name">Caldor Hydro Graphics</p>
      <p class="holder-name">Wade Caldor</p>
      <div class="divider"></div>
      <address class="contact contact--address" style="font-style: normal;">
        212 Mesa Ridge Road<br>
        Red Rock, TX 75402
      </address>
      <p class="contact contact--reach">
        555-014-2290<br>
        www.<span class="domain">caldorfx</span>.com<br>
        wade@caldorfx.com
      </p>
    </section>
  </main>
</body>
</html>
```